Business Card Design for Property Development Company Director

I am looking for a professional and unforgettable business card design for our Director of our Property Development Company.
Please see attached .pptx file to find out what information to include. You don't have to follow the exact format shown in the file - I am interested to see your creative flair using the information provided.

```html
<!DOCTYPE html>
<html lang="en">
<head>
<meta charset="utf-8">
<title>Halwen Property Group – Business Card</title>
<link href="https://fonts.googleapis.com/css2?family=Montserrat:ital,wght@0,300;0,400;0,500;0,600;1,400&display=swap" rel="stylesheet">
<style>
  :root {
    --page: #ffffff;
    --card: #232325;
    --card-light: #2e2e31;
    --band: #3d3d41;
    --ink: #ffffff;
    --brand-blue: #2f62ad;
    --brand-grey: #a6a6a8;
    --pill: #606063;
  }
  * { margin: 0; padding: 0; box-sizing: border-box; }
  html, body {
    width: 1200px; height: 1200px; overflow: hidden;
    background: var(--page);
    font-family: "Montserrat", sans-serif;
    color: var(--ink);
  }
  .card {
    position: absolute;
    left: 182px; width: 844px; height: 482px;
    background: var(--card);
    overflow: hidden;
  }
  .card--front { top: 113px; }
  .card--back { top: 612px; background: linear-gradient(180deg, #232325 0%, #28282a 55%, #232325 100%); }

  .front-shading { position: absolute; inset: 0; }

  .wordmark {
    position: absolute;
    display: flex; align-items: center; gap: 14px;
    font-weight: 600; letter-spacing: 1px; white-space: nowrap;
  }
  .wordmark__square { width: 30px; height: 30px; }
  .card--front .wordmark { left: 0; right: 0; justify-content: center; top: 94px; font-size: 34px; color: var(--brand-blue); }
  .card--front .wordmark__square { background: var(--brand-blue); }
  .card--back .wordmark { left: 0; right: 0; justify-content: center; top: 208px; font-size: 32px; color: var(--brand-grey); }
  .card--back .wordmark__square { background: var(--brand-grey); }

  .lead { position: absolute; left: 0; width: 50px; height: 1px; background: var(--ink); }
  .lead::after {
    content: ""; position: absolute; right: -2px; top: -2px;
    width: 5px; height: 5px; border-radius: 50%; background: var(--ink);
  }

  .person-name { position: absolute; left: 63px; top: 245px; font-size: 30px; font-weight: 300; white-space: nowrap; }
  .person-name strong { font-weight: 500; }
  .person-role { position: absolute; left: 63px; width: 239px; top: 286px; text-align: right; font-size: 19px; font-weight: 500; }
  .contact { position: absolute; left: 64px; font-size: 22px; font-weight: 300; white-space: nowrap; }
  .contact--phone { top: 341px; }
  .contact--email { top: 374px; }
  .licence { position: absolute; left: 0; right: 0; top: 435px; text-align: center; font-size: 17px; font-weight: 500; }

  .specialty {
    position: absolute; left: 0; right: 0; top: 25px;
    text-align: center; font-size: 20px; font-weight: 500; line-height: 23px;
  }
  .bracket { position: absolute; border: 0 solid var(--ink); }
  .bracket--left { left: 261px; top: 80px; width: 54px; height: 24px; border-left-width: 5px; border-bottom-width: 5px; }
  .bracket--right { left: 553px; top: 34px; width: 30px; height: 70px; border-right-width: 5px; border-bottom-width: 5px; }

  .web-strip { position: absolute; left: 226px; top: 293px; width: 392px; height: 27px; }
  .web-strip__text {
    position: absolute; left: 266px; width: 351px; top: 293px; height: 27px;
    line-height: 27px; text-align: center; font-size: 22px; font-weight: 400;
  }
  .invite {
    position: absolute; left: 0; right: 0; top: 434px;
    text-align: center; font-size: 21px; font-style: italic; font-weight: 400;
  }
</style>
</head>
<body>

<section class="card card--front">
  <svg class="front-shading" width="844" height="482" viewBox="0 0 844 482" aria-hidden="true">
    <defs>
      <linearGradient id="lowerTone" x1="0" y1="0" x2="1" y2="1">
        <stop offset="0" stop-color="#333336"/>
        <stop offset="0.6" stop-color="#2b2b2e"/>
        <stop offset="1" stop-color="#252528"/>
      </linearGradient>
    </defs>
    <polygon points="0,176 844,266 844,482 0,482" fill="url(#lowerTone)"/>
    <polygon points="0,176 844,266 844,280 0,191" fill="var(--band)"/>
  </svg>

  <div class="wordmark"><span class="wordmark__square"></span>HALWEN PROPERTY GROUP</div>

  <span class="lead" style="top:265px"></span>
  <p class="person-name"><strong>Daniel</strong> Marsh</p>
  <p class="person-role">Director</p>

  <span class="lead" style="top:355px"></span>
  <p class="contact contact--phone">0400 123 456</p>
  <span class="lead" style="top:389px"></span>
  <p class="contact contact--email">daniel@halwen.com.au</p>

  <p class="licence">Real Estate Lic: 1234567 &amp; 1234568</p>
</section>

<section class="card card--back">
  <p class="specialty">Property Development<br>&amp;<br>Site Acquisition Specialists</p>
  <span class="bracket bracket--left"></span>
  <span class="bracket bracket--right"></span>

  <div class="wordmark"><span class="wordmark__square"></span>HALWEN PROPERTY GROUP</div>

  <svg class="web-strip" width="392" height="27" viewBox="0 0 392 27" aria-hidden="true">
    <polygon points="0,0 10,0 22,26 12,26" fill="var(--pill)"/>
    <polygon points="20,0 30,0 42,26 32,26" fill="var(--pill)"/>
    <polygon points="40,0 386,0 392,26 52,26" fill="var(--pill)"/>
  </svg>
  <p class="web-strip__text">www.halwen.com.au</p>

  <p class="invite">Ask me about our INVESTMENT &amp; PARTNERSHIP opportunities</p>
</section>

</body>
</html>
```